Tailbrook Website Design

Need a website for a Dog Grooiming business. Please make it simular to these:

https://www.furvanto.com
https://haulnorix.com
https://meadowpetrin.com
https://www.drivelumo.com/search/

```html
<!DOCTYPE html>
<html lang="en">
<head>
<meta charset="utf-8">
<title>Tailbrook – Dog Grooming</title>
<link href="https://fonts.googleapis.com/css2?family=Poppins:wght@500;600;700&family=Roboto:wght@400;500;700&display=swap" rel="stylesheet">
<style>
:root{
  --royal:#24409a;
  --navy:#0a4a8f;
  --footer:#0e50a6;
  --green:#6dd69b;
  --ink:#111;
  --white:#fff;
  --grey:#e6e8ec;
  --canvas:#f4f5f7;
}
*{box-sizing:border-box;margin:0;padding:0}
html,body{width:1200px;height:3000px;overflow:hidden;background:var(--canvas);font-family:'Roboto',sans-serif;color:var(--ink)}
.page{position:absolute;left:147px;top:0;width:742px;height:2455px;background:var(--white);transform:scale(1.222);transform-origin:0 0;overflow:hidden}
.abs{position:absolute}
.photo{position:absolute}
.h-font{font-family:'Poppins',sans-serif}
.accent{color:var(--green)}
.blue{color:var(--royal)}

/* header */
.logo{left:22px;top:12px;display:flex;align-items:center;gap:8px}
.logo-mark{width:34px;height:34px;border-radius:50%;background:var(--royal)}
.logo-name{font-family:'Poppins',sans-serif;font-weight:600;font-size:17px;line-height:20px;color:#1b1b1b}
.topinfo{top:11px;font-size:8px;display:flex;align-items:center;gap:8px}
.topinfo svg{width:12px;height:12px}
.flag{width:26px;height:14px;background:linear-gradient(#c43 0 50%,#eee 50%);border-radius:1px}
.btn-contact{left:608px;top:5px;width:94px;height:25px;background:var(--royal);color:#fff;font-size:8px;font-weight:700;display:flex;align-items:center;justify-content:center}
.nav{left:0;top:60px;width:742px;height:48px;background:var(--royal)}
.nav a{position:absolute;top:19px;color:#fff;font-size:8px;text-decoration:none}

/* quote form */
.quote{left:431px;top:44px;width:274px;height:384px;background:var(--royal)}
.quote-head{height:81px;background:var(--green);color:#fff;font-family:'Roboto',sans-serif;font-weight:700;font-size:16px;line-height:20px;text-align:center;padding-top:15px}
.quote-tab{left:410px;top:45px;width:0;height:0;border-bottom:15px solid var(--green);border-left:21px solid transparent}
.field{position:absolute;background:#fff;font-size:8px;font-weight:500;display:flex;align-items:center;padding-left:9px}
.field b{color:#e02424;margin-left:3px}
.btn-green{position:absolute;background:var(--green);color:#fff;font-weight:500;display:flex;align-items:center;justify-content:center}

/* hero */
.hero-title{left:28px;top:210px;font-size:22px;font-weight:700;line-height:35px;color:#111}
.hero-sub{left:28px;top:286px;font-size:7px}

/* services */
.svc-title{left:408px;top:502px;font-size:21px;font-weight:700}
.svc-text{left:406px;top:556px;font-size:8px;line-height:10px}
.svc-item{position:absolute;display:flex;align-items:center;gap:10px;font-size:8px;font-weight:500;color:var(--royal);line-height:10px}
.svc-icon{width:46px;height:46px;border-radius:50%;background:var(--grey);display:flex;align-items:center;justify-content:center}

/* about */
.about{left:0;top:765px;width:742px;height:262px;background:var(--navy);color:#fff}
.about h2{position:absolute;left:57px;top:55px;font-family:'Poppins',sans-serif;font-weight:600;font-size:21px}
.about p{position:absolute;left:57px;font-size:8px;line-height:10.7px;width:295px}
.btn-outline{position:absolute;left:57px;top:201px;width:83px;height:24px;background:#fff;color:var(--navy);font-size:8px;display:flex;align-items:center;justify-content:center}

/* sections */
.sec-title{left:0;width:742px;text-align:center;font-family:'Poppins',sans-serif;font-weight:600;font-size:21px}
.testi{left:0;top:1615px;width:742px;height:344px;background:var(--navy)}
.card{position:absolute;top:1711px;width:255px;height:130px;background:#fff;border-radius:3px;font-size:7px;line-height:11px;padding:42px 22px 0 22px}
.card .q{position:absolute;left:28px;top:20px;font-family:'Poppins',sans-serif;font-size:36px;line-height:30px;color:var(--green);font-weight:700}
.card::after{content:"";position:absolute;left:26px;bottom:-14px;border-top:14px solid #fff;border-right:22px solid transparent}
.person{position:absolute;top:1868px;display:flex;align-items:center;gap:7px;color:#fff;font-size:7px;line-height:9px}
.avatar{width:41px;height:41px;border-radius:50%;background:linear-gradient(#e8ddd3,#b58f75);border:2px solid #fff}
.stars{color:#f7c624;letter-spacing:1px}
.arrow{position:absolute;top:1770px;width:26px;height:12px}

/* blogs */
.blog-box{position:absolute;width:166px;height:78px;background:#fff;box-shadow:0 2px 8px rgba(0,0,0,.12);padding:12px 16px 0 16px;font-size:6.5px;line-height:9px}
.blog-box h3{font-size:9px;font-weight:500;color:var(--royal);margin-bottom:3px}
.blog-box span{position:absolute;right:14px;bottom:8px;color:var(--royal);font-size:7px}

/* footer */
.footer{left:0;top:2272px;width:742px;height:183px;background:var(--footer);color:#fff}
.footer h4{position:absolute;top:28px;font-weight:500;font-size:14px}
.footer ul{position:absolute;top:58px;list-style:none;font-size:9px;line-height:12px}
.contact-row{position:absolute;display:flex;gap:10px;font-size:9px;line-height:12px}
.contact-row svg{width:10px;height:10px;flex:none;margin-top:1px}
.social{position:absolute;top:60px;width:11px;height:11px;border-radius:50%;border:1.5px solid #fff}
.rule{left:69px;top:150px;width:610px;height:1px;background:rgba(255,255,255,.6)}
.copy{left:0;top:161px;width:742px;text-align:center;font-size:6.5px}
</style>
</head>
<body>
<main class="page">

  <!-- header -->
  <header>
    <div class="abs logo"><span class="logo-mark"></span><span class="logo-name">Tailbrook</span></div>
    <div class="abs topinfo" style="left:290px">
      <svg viewBox="0 0 12 12"><circle cx="6" cy="6" r="5" fill="none" stroke="#24409a" stroke-width="1.4"/><path d="M1 6h10M6 1c-3 3-3 7 0 10M6 1c3 3 3 7 0 10" fill="none" stroke="#24409a" stroke-width="1"/></svg>
      <span>Your Location</span>
    </div>
    <div class="abs topinfo" style="left:403px"><span class="flag"></span><span>USA</span></div>
    <div class="abs topinfo" style="left:482px">
      <svg viewBox="0 0 12 12"><path d="M3 1l2 3-1.3 1.3a7 7 0 003 3L8 7l3 2-1.5 2C5 11 1 7 1 2.5z" fill="#24409a"/></svg>
      <span style="font-weight:700">0412-5580937</span>
    </div>
    <div class="abs btn-contact">Contect Us</div>
    <nav class="abs nav">
      <a style="left:75px">Home</a><a style="left:137px">About Us</a><a style="left:209px">Contect Us</a><a style="left:285px">Products</a><a style="left:352px">Blogs</a>
    </nav>
  </header>

  <!-- hero -->
  <section>
    <h1 class="abs hero-title h-font">Where Being <span class="blue">A Pet</span><br>Is Just <span class="blue">The Best</span></h1>
    <p class="abs hero-sub">A Great Place To Have Your Dog Groomed</p>
    <div class="btn-green" style="left:30px;top:310px;width:83px;height:24px;font-size:8px">CLICK HERE</div>
    <div class="photo" role="img" aria-label="Smiling golden retriever lying down" style="left:250px;top:170px;width:181px;height:250px;background:radial-gradient(ellipse at 55% 55%,#e8c89a 0%,#d9b07a 45%,rgba(255,255,255,0) 72%)"></div>
  </section>

  <div class="abs quote-tab"></div>
  <form class="abs quote">
    <div class="quote-head">Get Free Quotes From<br>Senior Specialists!</div>
    <div class="field" style="left:20px;top:114px;width:113px;height:41px">FIRST NAME<b>*</b></div>
    <div class="field" style="left:144px;top:114px;width:113px;height:41px">LAST NAME<b>*</b></div>
    <div class="field" style="left:20px;top:170px;width:113px;height:41px">PRIMARY PHONE<b>*</b></div>
    <div class="field" style="left:144px;top:170px;width:113px;height:41px">CELL PHONE<b>*</b></div>
    <div class="field" style="left:20px;top:220px;width:237px;height:46px">E-MAIL ADDRESS<b>*</b></div>
    <div class="field" style="left:20px;top:273px;width:237px;height:45px">STATE<b>*</b></div>
    <div class="btn-green" style="left:20px;top:327px;width:143px;height:42px;font-size:10px">CLICK HERE</div>
  </form>

  <!-- services -->
  <section>
    <div class="photo" role="img" aria-label="Small terrier being trimmed with comb and scissors" style="left:0;top:458px;width:378px;height:307px;background:linear-gradient(135deg,#5e5a55,#a58c6e 55%,#d8d4ce);clip-path:polygon(0 0,100% 0,70% 100%,0 100%)"></div>
    <h2 class="abs svc-title h-font">Our <span class="accent">Service</span></h2>
    <p class="abs svc-text">Lorem Ipsum Dolor Sit Amet, Consectetur Adipiscing Elit.<br>Consequat Sagittis Sed Felis, Orci Neque At Mauris,</p>
    <div class="svc-item" style="left:388px;top:608px"><span class="svc-icon"></span><span>Haircut &amp; Light<br>Dematting.</span></div>
    <div class="svc-item" style="left:552px;top:607px"><span class="svc-icon"></span><span>Brushing.</span></div>
    <div class="svc-item" style="left:385px;top:687px"><span class="svc-icon"></span><span>Nail Trim.</span></div>
    <div class="svc-item" style="left:552px;top:686px"><span class="svc-icon"></span><span>Shampoo</span></div>
  </section>

  <!-- about -->
  <section class="abs about">
    <h2>About Our Grooming</h2>
    <p style="top:93px">Lorem ipsum dolor sit amet, consectetur adipiscing elit. Tellus dictum ornare posuere quis montes, senectus pellentesque ullamcorper aliquet. Sed odio augue aliquam dignissim risus magna. Cursus.</p>
    <p style="top:136px">Lorem ipsum dolor sit amet, consectetur adipiscing elit. Tellus dictum ornare posuere quis montes, senectus pellentesque ullamcorper aliquet. Sed odio augue aliquam dignissim risus magna. Cursus. Lorem ipsum dolor sit amet, consectetur adipiscing elit.</p>
    <div class="btn-outline">LEARN MORE</div>
    <div class="abs" style="left:450px;top:29px;width:260px;height:173px;background:var(--green)"></div>
    <div class="photo" role="img" aria-label="Fluffy small dog resting on a wooden floor" style="left:474px;top:44px;width:250px;height:168px;background:linear-gradient(180deg,#ece4da,#d9c7b0 70%,#b58c62)"></div>
  </section>

  <!-- gallery -->
  <section>
    <h2 class="abs sec-title" style="top:1078px">Our <span class="accent">Gallary</span></h2>
    <div class="photo" role="img" aria-label="Groomer trimming a dark poodle" style="left:33px;top:1144px;width:243px;height:162px;background:linear-gradient(135deg,#c9a874,#3c2f2a 60%,#9b7a52)"></div>
    <div class="photo" role="img" aria-label="Small dog held in hands outdoors" style="left:303px;top:1144px;width:157px;height:194px;background:linear-gradient(160deg,#6f8a55,#8b5e3c 55%,#8a6aa0)"></div>
    <div class="photo" role="img" aria-label="Groomer brushing a small dog on a table" style="left:486px;top:1144px;width:236px;height:162px;background:linear-gradient(120deg,#f2f2f2,#d9dde0 50%,#c98f86)"></div>
    <div class="photo" role="img" aria-label="Wet terrier after a bath" style="left:39px;top:1325px;width:237px;height:240px;background:linear-gradient(135deg,#f1ece8,#c79a67 55%,#f0ebe6)"></div>
    <div class="photo" role="img" aria-label="Groomer trimming a dark poodle" style="left:289px;top:1345px;width:184px;height:220px;background:linear-gradient(160deg,#c9a874,#3c2f2a 60%,#9b7a52)"></div>
    <div class="photo" role="img" aria-label="Wet terrier after a bath" style="left:486px;top:1325px;width:237px;height:240px;background:linear-gradient(135deg,#f1ece8,#c79a67 55%,#f0ebe6)"></div>
  </section>

  <!-- testimonials -->
  <section>
    <div class="abs testi"></div>
    <h2 class="abs sec-title" style="top:1655px;color:#fff">OUR <span class="accent">TESTIMONIAL</span></h2>
    <svg class="arrow" style="left:72px" viewBox="0 0 26 12"><path d="M25 6H2M7 1L2 6l5 5" fill="none" stroke="#fff" stroke-width="1.3"/></svg>
    <svg class="arrow" style="left:677px" viewBox="0 0 26 12"><path d="M1 6h23M19 1l5 5-5 5" fill="none" stroke="#fff" stroke-width="1.3"/></svg>
    <div class="card" style="left:124px"><span class="q">&ldquo;</span>&emsp;&emsp;&emsp;&emsp;&ensp;Lorem Ipsum Dolor Sit Amet, Consectetur Adipiscing Odio Ultrices Amet, Congue Integer Any Nibh. Amet, Eget Tristique Vitae A Sed Venenatis. Dictumst Eros Id Vitae Orci Id. Senectus Senectus Parturient Any Time &nbsp;Diam, Namtristique Vitae A Sed Venenatis. Dictumst Dictumst Dictumst Eros Id</div>
    <div class="card" style="left:395px"><span class="q">&ldquo;</span>&emsp;&emsp;&emsp;&emsp;&ensp;Lorem Ipsum Dolor Sit Amet, Consectetur Adipiscing Odio Ultrices Amet, Congue Integer Any Nibh. Amet, Eget Tristique Vitae A Sed Venenatis. Dictumst Eros Id Vitae Orci Id. Senectus Senectus Parturient Any Time &nbsp;Diam, Namtristique Vitae A Sed Venenatis. Dictumst Dictumst Dictumst Eros Id</div>
    <div class="person" style="left:121px"><span class="avatar" role="img" aria-label="Customer portrait"></span><span><b>Lorem Ipsum</b><br>Lorem Ipsum<br><span class="stars">★★★★★</span></span></div>
    <div class="person" style="left:394px"><span class="avatar" role="img" aria-label="Customer portrait"></span><span><b>Lorem Ipsum</b><br>Lorem Ipsum<br><span class="stars">★★★★★</span></span></div>
  </section>

  <!-- blogs -->
  <section>
    <h2 class="abs sec-title" style="top:2024px">OUR <span class="accent">BLOGS</span></h2>
    <div class="photo" role="img" aria-label="Groomer brushing a small dog" style="left:29px;top:2068px;width:188px;height:120px;background:linear-gradient(120deg,#f2f2f2,#d9dde0 50%,#c98f86)"></div>
    <div class="blog-box" style="left:73px;top:2152px"><h3>Brushing</h3>Lorem ipsum dolor sit amet, consectetur adipiscing elit. Quis laoreet posuere purus tincidunt vitae.<span>Learn More→</span></div>
    <div class="photo" role="img" aria-label="Groomer trimming a dark poodle" style="left:270px;top:2068px;width:190px;height:130px;background:linear-gradient(135deg,#c9a874,#3c2f2a 60%,#9b7a52)"></div>
    <div class="blog-box" style="left:316px;top:2162px"><h3>Hair Cut</h3>Lorem ipsum dolor sit amet, consectetur adipiscing elit. Quis laoreet posuere purus tincidunt vitae.<span>Learn More→</span></div>
    <div class="photo" role="img" aria-label="Brown dog being shampooed" style="left:512px;top:2068px;width:190px;height:130px;background:linear-gradient(135deg,#4a3128,#7a4a36 50%,#d9d4cf)"></div>
    <div class="blog-box" style="left:558px;top:2162px"><h3>Shampoo</h3>Lorem ipsum dolor sit amet, consectetur adipiscing elit. Quis laoreet posuere purus tincidunt vitae.<span>Learn More→</span></div>
  </section>

  <!-- footer -->
  <footer class="abs footer">
    <div class="abs logo" style="left:62px;top:14px"><span class="logo-mark" style="background:#fff"></span><span class="logo-name" style="color:#fff">Tailbrook</span></div>
    <p class="abs" style="left:70px;top:66px;width:140px;font-size:6.5px;line-height:9.5px">lorem ipsum dolor sit amet, consectetur adipiscing elit. viverra et pellentesque leo imperdiet quis. a diam ut natoque amet sodales. id amet, viverra vitae et enim.</p>
    <h4 style="left:254px">QUICK LINKS</h4>
    <ul style="left:257px;top:59px"><li>Home</li><li>About Us</li><li>Services</li><li>Blog</li><li>Testimonial</li></ul>
    <h4 style="left:396px">CONTACT US</h4>
    <div class="contact-row" style="left:397px;top:56px"><svg viewBox="0 0 12 12"><path d="M3 1l2 3-1.3 1.3a7 7 0 003 3L8 7l3 2-1.5 2C5 11 1 7 1 2.5z" fill="#fff"/></svg><span>5103-2294-61</span></div>
    <div class="contact-row" style="left:397px;top:81px"><svg viewBox="0 0 12 12"><rect x="1" y="2.5" width="10" height="7" fill="none" stroke="#fff"/><path d="M1 3l5 4 5-4" fill="none" stroke="#fff"/></svg><span>hello@tailbrookgrooming.com</span></div>
    <div class="contact-row" style="left:397px;top:103px"><svg viewBox="0 0 12 12"><path d="M11 1L1 5.5l4.5 1.5L7 11z" fill="#fff"/></svg><span>Street no 12 near Maple Plaza,<br>Fernvale USA</span></div>
    <h4 style="left:583px">FOLLOW US</h4>
    <span class="social" style="left:584px"></span><span class="social" style="left:610px"></span><span class="social" style="left:635px"></span><span class="social" style="left:661px"></span>
    <div class="abs rule"></div>
    <p class="abs copy">Copyright 2021 Tailbrook All Rights Reserved</p>
  </footer>

</main>
</body>
</html>
```